Business card design needed

The company name is Pellwick Architects. We are an architectural company based in Melbourne,Australia that has a mix of client base from health care, commercial office, aged care, multi-residential, single residential and retail. Design type is contemporary.

Suggest the base colours need to be black and white. Please leave an area on the back of the card available for handwritten notes.

Target Market(s)

Generally corporate, aged 30 to 65

Industry/Entity Type

Residential

Contact Information for Business Card

Pellwick Architects
Dane Pellwick
7 Horbury Street
Northvale VIC 3059
T (03) 9572 4016
M 0431 607 295
E dp@pellwickarc.com.au

Logo Text

PA

Logo styles of interest
Emblem Logo
Abstract Logo
Lettermark Logo
Requirements
Must have
• I am having trouble attaching a sketch so would really appreciate your effort to try the following brief.

Black and White (B&W)
Would like different card cutout profile. Logo Example, use the half circle curve of the G to form the left edge of the card with no margin. The A is to sit inside the G, connected to the G by its horizontal. The A has its cross bar and lower right leg removed. Card in black, text in white.

Back of card to be black text on white background with services provided.

Client Focused Service
Architecture and Design
Functional Planning
Town Planning
Feasability Studies
Contract Documentation
Contract Administration
Project Management

Simple elegant text, Ariel or similar
Nice to have
• Integrated logo and card cut-out.

Card base black on front, white on back
Should not have
• Too many colours
Fussy details

```html
<!DOCTYPE html>
<html lang="en">
<head>
<meta charset="utf-8">
<title>Pellwick Architects – Business Card</title>
<link rel="stylesheet" href="https://fonts.googleapis.com/css2?family=Jost:wght@400;500&display=swap">
<style>
  :root {
    --backdrop: #2b2b2b;
    --card-back: #f7f7f7;
    --card-front: #0c0c0c;
    --ink-dark: #1a1a1a;
    --ink-mid: #4a4a4a;
    --ink-light: #ffffff;
    --ink-soft: #d6d6d6;
    --rule-dark: #bdbdbd;
    --rule-light: #5a5a5a;
  }
  * { box-sizing: border-box; margin: 0; padding: 0; }
  html, body {
    width: 1200px; height: 900px; overflow: hidden;
    background: var(--backdrop);
    font-family: "Jost", Arial, sans-serif;
  }
  .sheet {
    width: 1200px; height: 900px;
    display: flex; flex-direction: column;
    align-items: center; justify-content: center; gap: 36px;
  }
  .card {
    width: 660px; height: 400px;
    position: relative; overflow: hidden;
  }
  .card--back { background: var(--card-back); }
  .card--front { background: var(--card-front); }

  /* Back: services + notes */
  .services {
    position: absolute; left: 56px; top: 54px;
    color: var(--ink-mid);
  }
  .services__title {
    font-size: 25px; font-weight: 500; color: var(--ink-dark);
    margin-bottom: 8px;
  }
  .services__list { list-style: none; }
  .services__item {
    font-size: 21px; line-height: 32px;
    position: relative; padding-left: 26px;
  }
  .services__item::before {
    content: ""; position: absolute; left: 0; top: 13px;
    width: 7px; height: 7px; border-radius: 50%;
    background: var(--ink-dark);
  }
  .notes {
    position: absolute; left: 400px; top: 54px;
    width: 210px; height: 292px;
    border-left: 1px solid var(--rule-dark);
    padding-left: 24px;
  }
  .notes__label {
    font-size: 16px; letter-spacing: 2px; text-transform: uppercase;
    color: var(--ink-mid); margin-bottom: 6px;
  }
  .notes__line {
    height: 42px; border-bottom: 1px solid var(--rule-dark);
  }

  /* Front: identity */
  .brand {
    position: absolute; top: 92px; left: 0; right: 0;
    display: flex; align-items: center; justify-content: center; gap: 16px;
  }
  .brand__dot {
    width: 54px; height: 54px; border-radius: 50%;
    border: 4px solid var(--ink-light);
  }
  .brand__name {
    font-size: 40px; font-weight: 400; color: var(--ink-light);
    letter-spacing: 1px;
  }
  .holder {
    position: absolute; left: 80px; top: 258px;
    font-size: 27px; font-weight: 500; color: var(--ink-light);
  }
  .divider {
    position: absolute; left: 300px; top: 210px;
    width: 1px; height: 130px; background: var(--rule-light);
  }
  .contact {
    position: absolute; left: 330px; top: 205px;
    list-style: none; color: var(--ink-soft);
    font-size: 22px; line-height: 28px;
  }
  .contact__row { display: flex; align-items: flex-start; gap: 14px; }
  .contact__icon { width: 20px; height: 20px; margin-top: 4px; flex: none; fill: var(--ink-soft); }
</style>
</head>
<body>
<main class="sheet">

  <section class="card card--back" aria-label="Card back">
    <div class="services">
      <h2 class="services__title">Client Focused Service</h2>
      <ul class="services__list">
        <li class="services__item">Architecture + Design</li>
        <li class="services__item">Functional Planning</li>
        <li class="services__item">Town Planning</li>
        <li class="services__item">Feasibility Studies</li>
        <li class="services__item">Contract Documentation</li>
        <li class="services__item">Contract Administration</li>
        <li class="services__item">Project Management</li>
      </ul>
    </div>
    <div class="notes" aria-label="Notes area">
      <p class="notes__label">Notes</p>
      <div class="notes__line"></div>
      <div class="notes__line"></div>
      <div class="notes__line"></div>
      <div class="notes__line"></div>
      <div class="notes__line"></div>
      <div class="notes__line"></div>
    </div>
  </section>

  <section class="card card--front" aria-label="Card front">
    <div class="brand">
      <span class="brand__dot"></span>
      <span class="brand__name">Pellwick Architects</span>
    </div>

    <p class="holder">Dane Pellwick</p>
    <span class="divider"></span>

    <ul class="contact">
      <li class="contact__row">
        <svg class="contact__icon" viewBox="0 0 20 20"><path d="M10 1a6 6 0 0 0-6 6c0 4.5 6 12 6 12s6-7.5 6-12a6 6 0 0 0-6-6zm0 8.5A2.5 2.5 0 1 1 10 4.5a2.5 2.5 0 0 1 0 5z"/></svg>
        <span>7 Horbury Street,<br>Northvale VIC 3059</span>
      </li>
      <li class="contact__row">
        <svg class="contact__icon" viewBox="0 0 20 20"><path d="M2 7c0-2 3.5-3.5 8-3.5S18 5 18 7v1.5h-4V7H6v1.5H2zM5 10h10l2 7H3z"/></svg>
        <span>(03) 9572 4016</span>
      </li>
      <li class="contact__row">
        <svg class="contact__icon" viewBox="0 0 20 20"><path d="M6 1h8a1 1 0 0 1 1 1v16a1 1 0 0 1-1 1H6a1 1 0 0 1-1-1V2a1 1 0 0 1 1-1zm1 2v6h6V3zm0 8v2h2v-2zm4 0v2h2v-2zm-4 3v2h2v-2zm4 0v2h2v-2z"/></svg>
        <span>0431 607 295</span>
      </li>
      <li class="contact__row">
        <svg class="contact__icon" viewBox="0 0 20 20"><path d="M2 4h16v12H2zm1.5 1.5v.4L10 10.5l6.5-4.6v-.4zm0 2.2v6.8h13V7.7L10 12.3z"/></svg>
        <span>dp@pellwickarc.com.au</span>
      </li>
    </ul>
  </section>

</main>
</body>
</html>
```